Maple Lantern Business Card

Design of business cards

Target Market(s)

We are aiming as small business owners who need anything from basic business structures, website plans, business processes and quality assurance.

Industry/Entity Type

Business

Colors

Designer to choose colors to be used in the design.

Requirements
Nice to have
• I would prefer one side of the card to use the green from the logo. Prefer to have the same font as the logo.

```html
<!DOCTYPE html>
<html lang="en">
<head>
<meta charset="utf-8">
<title>Maple Lantern Business Card</title>
<link rel="stylesheet" href="https://fonts.googleapis.com/css2?family=Cinzel:wght@400;600&display=swap">
<style>
  :root {
    --lime: #a6cd3c;
    --ink: #2b2b2b;
    --slate: #58595b;
    --paper: #ffffff;
    --backdrop: #e9eaec;
    --social: #4a8fc0;
  }
  * { margin: 0; padding: 0; box-sizing: border-box; }
  html, body { width: 1200px; height: 960px; overflow: hidden; }
  body {
    background: var(--backdrop);
    font-family: "Cinzel", "Times New Roman", serif;
    display: flex;
    flex-direction: column;
    align-items: center;
    justify-content: center;
    gap: 56px;
  }
  .card {
    width: 660px;
    height: 377px;
    position: relative;
    box-shadow: 0 6px 18px rgba(0,0,0,0.18);
  }
  /* Front */
  .card-front {
    background: var(--lime);
    display: flex;
    align-items: center;
    justify-content: center;
  }
  .front-wordmark {
    display: flex;
    align-items: center;
    gap: 22px;
    color: var(--paper);
  }
  .front-wordmark .mark-dot {
    width: 26px; height: 26px; border-radius: 50%;
    background: var(--paper);
  }
  .front-wordmark .name {
    font-size: 58px;
    font-weight: 600;
    letter-spacing: 2px;
  }
  /* Back */
  .card-back {
    background: var(--paper);
    padding: 34px 40px 30px 44px;
    color: var(--ink);
  }
  .brand {
    display: flex;
    align-items: center;
    gap: 12px;
    color: var(--lime);
    font-size: 26px;
    font-weight: 600;
    letter-spacing: 1px;
  }
  .brand .mark-square {
    width: 16px; height: 16px; background: var(--lime);
  }
  .person { margin-top: 40px; }
  .person .person-name { font-size: 21px; font-weight: 600; letter-spacing: 1px; }
  .person .person-role { font-size: 15px; color: var(--lime); letter-spacing: 1px; }
  .contacts { margin-top: 18px; list-style: none; }
  .contacts li {
    display: flex; align-items: center; gap: 12px;
    font-size: 14px; line-height: 20px; letter-spacing: 0.5px;
  }
  .contacts svg { width: 13px; height: 13px; flex: none; }
  .address { margin-top: 16px; font-size: 15px; letter-spacing: 0.5px; }
  .socials {
    position: absolute; right: 44px; bottom: 34px;
    display: flex; gap: 14px; align-items: center;
  }
  .socials span { width: 20px; height: 20px; background: var(--social); border-radius: 3px; }
</style>
</head>
<body>
  <section class="card card-front" aria-label="Card front">
    <div class="front-wordmark">
      <span class="mark-dot"></span>
      <span class="name">Maple Lantern</span>
    </div>
  </section>

  <section class="card card-back" aria-label="Card back">
    <div class="brand">
      <span class="mark-square"></span>
      <span>Maple Lantern Consulting</span>
    </div>
    <div class="person">
      <p class="person-name">DANIEL REYES</p>
      <p class="person-role">Founder &amp; Ceo</p>
    </div>
    <ul class="contacts">
      <li>
        <svg viewBox="0 0 16 16" fill="none" stroke="#888" stroke-width="1.4"><path d="M4 2h3l1 3-2 1a8 8 0 0 0 4 4l1-2 3 1v3a1 1 0 0 1-1 1A12 12 0 0 1 3 3a1 1 0 0 1 1-1z"/></svg>
        021 555 01734
      </li>
      <li>
        <svg viewBox="0 0 16 16" fill="none" stroke="#888" stroke-width="1.4"><rect x="1.5" y="3.5" width="13" height="9"/><path d="M1.5 3.5 8 9l6.5-5.5"/></svg>
        HELLO@MAPLELANTERN.COM
      </li>
      <li>
        <svg viewBox="0 0 16 16" fill="none" stroke="#888" stroke-width="1.4"><circle cx="8" cy="8" r="6.5"/><path d="M1.5 8h13M8 1.5c3 3 3 10 0 13M8 1.5c-3 3-3 10 0 13"/></svg>
        WWW.MAPLELANTERN.COM
      </li>
    </ul>
    <p class="address">48 Harlow Avenue, California 90412</p>
    <div class="socials" aria-label="Social links">
      <span></span><span></span><span></span>
    </div>
  </section>
</body>
</html>
```